Business Card Project

Hello,

Please find attached files for use for our business card design.

We have attached all the version of the trade licensing council to the project for insertion onto our business card.

Details to be on the card are:
We are a construction management company. Please ensure that there is space to add our personal contact details. We would like the cards to be double sided with our logo on one side and our details on the other

Thanks,

Marcus

Good Evening,

Please ensure with all design submissions, that the 'certified works overseer' logo is on the card designs.

Thanks,

Marcus

Industry/Entity Type

Construction

```html
<!DOCTYPE html>
<html lang="en">
<head>
<meta charset="utf-8">
<title>Norcrest Group – Business Card</title>
<link href="https://fonts.googleapis.com/css2?family=Montserrat:wght@400;500;700;800&display=swap" rel="stylesheet">
<style>
  :root {
    --brown-dark: #3a241d;
    --brown: #5a3a2e;
    --brown-accent: #6b4434;
    --paper: #ffffff;
    --ink: #2a2a2a;
    --muted: #8a8a8a;
    --faint: #ece9e6;
    --stage: #e9e6e2;
  }
  * { box-sizing: border-box; margin: 0; padding: 0; }
  html, body {
    width: 1200px; height: 784px; overflow: hidden;
    background: var(--stage);
    font-family: "Montserrat", sans-serif;
  }
  .canvas {
    position: relative; width: 1200px; height: 784px;
    display: flex; align-items: center; justify-content: center; gap: 40px;
  }
  .card {
    position: relative; width: 540px; height: 309px; overflow: hidden;
    box-shadow: 0 6px 18px rgba(0,0,0,.18);
  }

  /* Back side */
  .card-back { background: var(--brown-dark); }
  .back-brand {
    position: absolute; left: 0; right: 0; top: 112px;
    display: flex; align-items: center; justify-content: center; gap: 22px;
  }
  .back-rule { width: 70px; height: 3px; background: var(--paper); }
  .back-name {
    color: var(--paper); font-weight: 800; font-size: 52px; letter-spacing: 1px; line-height: 1;
  }
  .back-tagline {
    position: absolute; left: 0; right: 0; top: 176px; text-align: center;
    color: #b9aaa3; font-size: 9px; letter-spacing: 1px;
  }

  /* Front side */
  .card-front { background: var(--paper); }
  .band-top { position: absolute; left: 0; right: 0; top: 0; height: 12px; background: var(--brown-dark); }
  .band-bottom { position: absolute; left: 0; right: 0; bottom: 0; height: 38px; background: var(--brown-dark); }
  .faint-mark {
    position: absolute; right: -10px; top: 60px;
    color: var(--faint); font-weight: 800; font-size: 92px; line-height: 1;
  }
  .front-brand { position: absolute; left: 38px; top: 46px; }
  .front-name { color: var(--brown); font-weight: 800; font-size: 38px; line-height: 1; }
  .front-tagline { color: var(--muted); font-size: 7px; margin-top: 4px; margin-left: 2px; }
  .front-rule {
    position: absolute; left: 215px; top: 72px; width: 90px; height: 1px;
    background: linear-gradient(90deg, #bbb, transparent);
  }
  .person { position: absolute; left: 38px; top: 132px; }
  .person-name { color: var(--brown-accent); font-weight: 700; font-size: 17px; }
  .person-role { color: var(--muted); font-size: 10px; margin-top: 1px; }
  .contacts { position: absolute; left: 38px; top: 172px; list-style: none; }
  .contacts li {
    display: flex; align-items: center; gap: 8px;
    color: var(--ink); font-size: 13px; line-height: 17px;
  }
  .contacts svg { width: 13px; height: 13px; fill: var(--ink); flex: none; }
  .cert-badge {
    position: absolute; right: 38px; top: 178px; width: 44px; height: 44px;
    border-radius: 50%; border: 3px solid #555; background: var(--paper);
  }
</style>
</head>
<body>
<main class="canvas">

  <section class="card card-back" aria-label="Card back">
    <div class="back-brand">
      <span class="back-rule"></span>
      <span class="back-name">NORCREST</span>
      <span class="back-rule"></span>
    </div>
    <div class="back-tagline">Group</div>
  </section>

  <section class="card card-front" aria-label="Card front">
    <div class="band-top"></div>
    <div class="faint-mark" aria-hidden="true">NORCREST</div>

    <div class="front-brand">
      <div class="front-name">NORCREST</div>
      <div class="front-tagline">Group</div>
    </div>
    <div class="front-rule"></div>

    <div class="person">
      <div class="person-name">Dana Whitlow</div>
      <div class="person-role">Manager</div>
    </div>

    <ul class="contacts">
      <li>
        <svg viewBox="0 0 24 24"><path d="M6.6 10.8c1.4 2.8 3.8 5.1 6.6 6.6l2.2-2.2c.3-.3.7-.4 1-.2 1.1.4 2.3.6 3.6.6.6 0 1 .4 1 1V20c0 .6-.4 1-1 1C10.6 21 3 13.4 3 4c0-.6.4-1 1-1h3.5c.6 0 1 .4 1 1 0 1.3.2 2.5.6 3.6.1.3 0 .7-.2 1L6.6 10.8z"/></svg>
        555-210-4417
      </li>
      <li>
        <svg viewBox="0 0 24 24"><path d="M7 2h10a2 2 0 0 1 2 2v16a2 2 0 0 1-2 2H7a2 2 0 0 1-2-2V4a2 2 0 0 1 2-2zm0 3v13h10V5H7zm5 14.2a1 1 0 1 0 0 2 1 1 0 0 0 0-2z"/></svg>
        555-210-8862
      </li>
      <li>
        <svg viewBox="0 0 24 24"><path d="M12 2a10 10 0 1 0 0 20 10 10 0 0 0 0-20zm6.9 6h-3a15 15 0 0 0-1.3-3.9A8 8 0 0 1 18.9 8zM12 4c.8 1.2 1.5 2.5 1.9 4h-3.8c.4-1.5 1.1-2.8 1.9-4zM4.3 14a8 8 0 0 1 0-4h3.4a16 16 0 0 0 0 4H4.3zm.8 2h3a15 15 0 0 0 1.3 3.9A8 8 0 0 1 5.1 16zm3-8h-3a8 8 0 0 1 4.3-3.9A15 15 0 0 0 8.1 8zM12 20c-.8-1.2-1.5-2.5-1.9-4h3.8c-.4 1.5-1.1 2.8-1.9 4zm2.3-6H9.7a14 14 0 0 1 0-4h4.6a14 14 0 0 1 0 4zm.3 5.9a15 15 0 0 0 1.3-3.9h3a8 8 0 0 1-4.3 3.9zm1.7-5.9a16 16 0 0 0 0-4h3.4a8 8 0 0 1 0 4h-3.4z"/></svg>
        www.norcrestbuild.com
      </li>
      <li>
        <svg viewBox="0 0 24 24"><path d="M3 5h18a1 1 0 0 1 1 1v12a1 1 0 0 1-1 1H3a1 1 0 0 1-1-1V6a1 1 0 0 1 1-1zm1 2.4V17h16V7.4l-8 5.3-8-5.3zM5.4 7 12 11.4 18.6 7H5.4z"/></svg>
        info@norcrestbuild.com
      </li>
      <li>
        <svg viewBox="0 0 24 24"><path d="M12 3 2 12h3v8h5v-5h4v5h5v-8h3L12 3z"/></svg>
        2280 Alder Ridge Rd. Canada
      </li>
    </ul>

    <div class="cert-badge" role="img" aria-label="Certified works overseer badge"></div>
    <div class="band-bottom"></div>
  </section>

</main>
</body>
</html>
```